Tidewell building company Business card design

I need a business card design for my company. I have a logo but dont have business cards with our logo..

www.tidewellbuildingco.com.au

The logo is on the website

I need the same details as this design I have attached. we have changed the logo and colours. just like the website

```html
<!DOCTYPE html>
<html lang="en">
<head>
<meta charset="utf-8">
<title>Tidewell Building – Business Card</title>
<link rel="stylesheet" href="https://fonts.googleapis.com/css2?family=Cormorant+SC:wght@600;700&family=Lato:wght@400&display=swap">
<style>
  :root {
    --page-bg: #d9d6d1;
    --card-bg: #f1f2f2;
    --card-edge: #e3e5e6;
    --ink: #1c232a;
    --brand-blue: #2f78b3;
    --wave-grey: #9a9b9e;
    --wave-blue-top: #3c86b7;
    --wave-blue-deep: #0e557f;
    --tag-ink: #2c3e4c;
    --copper: #c08f80;
  }
  * { margin: 0; padding: 0; box-sizing: border-box; }
  html, body { width: 1200px; height: 970px; overflow: hidden; }
  body { background: var(--page-bg); position: relative; }

  .business-card {
    position: absolute;
    left: 60px; top: 185px;
    width: 1080px; height: 600px;
    background: var(--card-bg);
    border: 1px solid var(--card-edge);
    overflow: hidden;
    box-shadow: 0 12px 40px rgba(0,0,0,0.18);
  }
  .card-wave { position: absolute; left: 0; top: 0; width: 1080px; height: 600px; }

  .brand {
    position: absolute;
    left: 62px; top: 150px;
    width: 260px;
    text-align: center;
  }
  .brand-square {
    display: block;
    width: 46px; height: 46px;
    margin: 0 auto 22px;
    background: var(--brand-blue);
  }
  .brand-name {
    font-family: "Cormorant SC", serif;
    font-weight: 600;
    font-size: 44px;
    line-height: 1.02;
    letter-spacing: 2px;
    color: var(--brand-blue);
  }

  .holder {
    position: absolute;
    right: 61px; top: 88px;
    text-align: right;
  }
  .holder-name {
    font-family: "Cormorant SC", serif;
    font-weight: 700;
    font-size: 34px;
    letter-spacing: 1.5px;
    color: var(--ink);
  }
  .holder-role {
    font-family: "Lato", sans-serif;
    font-size: 27px;
    letter-spacing: 0.5px;
    color: var(--brand-blue);
    margin-top: 2px;
  }

  .services {
    position: absolute;
    left: 30px; top: 426px;
    width: 450px;
    text-align: center;
    font-family: "Lato", sans-serif;
    font-size: 21px;
    line-height: 30px;
    color: var(--tag-ink);
  }

  .divider {
    position: absolute;
    left: 502px; top: 388px;
    width: 3px; height: 158px;
    background: linear-gradient(to bottom, rgba(192,143,128,0), var(--copper) 20%, var(--copper) 80%, rgba(192,143,128,0));
  }

  .contacts {
    position: absolute;
    left: 552px; top: 420px;
    list-style: none;
    font-family: "Lato", sans-serif;
    font-size: 27px;
    color: var(--ink);
  }
  .contacts li {
    display: flex;
    align-items: center;
    height: 43px;
  }
  .contacts svg { width: 32px; height: 32px; margin-right: 10px; flex: none; }
</style>
</head>
<body>
  <div class="business-card">
    <svg class="card-wave" viewBox="0 0 1080 600" aria-hidden="true">
      <defs>
        <linearGradient id="blueFill" x1="0" y1="0" x2="0" y2="1">
          <stop offset="0" stop-color="var(--wave-blue-top)"/>
          <stop offset="1" stop-color="var(--wave-blue-deep)"/>
        </linearGradient>
      </defs>
      <path d="M0 452 Q 528 140 1080 452 L1080 600 L0 600 Z" fill="var(--wave-grey)"/>
      <path d="M0 478 Q 528 180 1080 478 L1080 600 L0 600 Z" fill="url(#blueFill)"/>
      <path d="M0 478 Q 528 180 1080 478 L1080 600 L0 600 Z" fill="#ffffff" opacity="0.35"/>
    </svg>

    <div class="brand">
      <span class="brand-square"></span>
      <div class="brand-name">Tidewell<br>Building</div>
    </div>

    <div class="holder">
      <div class="holder-name">Marek Dolan</div>
      <div class="holder-role">Director</div>
    </div>

    <p class="services">New Homes, Addition &amp; Renovation<br>Domestic &amp; Commercial Builders</p>

    <div class="divider"></div>

    <ul class="contacts">
      <li>
        <svg viewBox="0 0 32 32" aria-hidden="true"><path d="M4 12 Q16 4 28 12 L26 15 L21 14 L20 11 Q16 10 12 11 L11 14 L6 15 Z" fill="var(--copper)"/><rect x="8" y="16" width="16" height="11" rx="2" fill="var(--copper)"/><circle cx="16" cy="21.5" r="3" fill="var(--card-bg)" opacity="0.7"/></svg>
        9312 4570
      </li>
      <li>
        <svg viewBox="0 0 32 32" aria-hidden="true"><rect x="9" y="3" width="14" height="26" rx="2.5" fill="none" stroke="var(--copper)" stroke-width="2.2"/><line x1="14" y1="25" x2="18" y2="25" stroke="var(--copper)" stroke-width="2"/></svg>
        0412558903 (Marek)
      </li>
      <li>
        <svg viewBox="0 0 32 32" aria-hidden="true"><rect x="4" y="8" width="24" height="16" fill="var(--copper)"/><path d="M4 8 L16 18 L28 8" fill="none" stroke="var(--card-bg)" stroke-width="1.6" opacity="0.8"/></svg>
        info@tidewellbuildingco.com.au
      </li>
    </ul>
  </div>
</body>
</html>
```